Website: Brightkeel Business Consultants, Qianhai SEZ, China

Our client is a business consultancy firm and will be the first to set up in the Qianhai Shenzhen-Hong Kong Modern Service Industry Cooperation Zone, China So we need a corporate website concept that engages service, finance and technology sector companies. The company can provide all the necessary services needed to set up shop in Qianhai. They are looking for a modern, international, reliable and strong image.

Here are some websites for reference prupose:

http://www.vornamesh.com/ (we like the dynamic banner and clear, clean layout of this website)

http://www.plendaradvisory.com/ (we like the background city image, use of light font, hover over menu functions and color scheme - purple and grey)

http://www.quolb.com/ (we like the simplicity of this website, clear lines and we like the dynamic banner)
Updates

Hello, We are currently undecided between three logo designs.  All three have been uploaded to the design brief so that you can use them as reference for the website design. Thx

Also please take note of the addition menu selection 'About Qianhai'. Thx

Hello all Designers, First of all we want thank you for participating in our website competition, the calibre of design was high and we appreciated the expedience. Our company is Lumenpath Web Design and Internet Marketing based in Shenzhen, China. We anticipate rapid growth in the Chinese domestic market as the country shifts in to a service sector economy. We hope to continue building reliable working relationships with you based on idea sharing and constructive feedback. Once again, Thankyou, LP Team

Target Market(s)

International finance and technology companies looking to set up in Qianhai Special Economic Zone, China

Industry/Entity Type

Finance

Requirements
Must have
• Initial design for home page and in later selection stages a secondary page will be required.

The design should be for PSD concepts only no code!

Menu bar, Photo banner -
A. Photo banner and text overlay,
B.Photo Banner and text description to left or right.

Social Connect icons, Site search bar (top right), Logo space (top left).

Menu bar at top with Home, About Us, About Qianhai, Services, Portfolio, Partners, Our Team Contact Us.

Standard 3-4 box layout - Banner at top and 2-3 boxes under banner.

Colour scheme- A. Purple and Blue, must have light background/body
B. Shades of white, black and grey.

Simple, clear, clean, sharp.

```html
<!DOCTYPE html>
<html lang="en">
<head>
<meta charset="utf-8">
<title>Brightkeel Business Consulting</title>
<link rel="stylesheet" href="https://fonts.googleapis.com/css2?family=Questrial&family=Arimo:wght@400&display=swap">
<style>
:root{
  --magenta:#b5138f;
  --teal:#1b8cb0;
  --teal-dark:#1d6f8a;
  --charcoal:#3a3a3a;
  --panel-title:#d4d4d4;
  --body-text:#666;
  --top-band:#e6e6e6;
  --footer-bg:#f4f3f3;
  --footer-text:#555;
  --white:#fff;
}
*{box-sizing:border-box;margin:0;padding:0}
html,body{width:1200px;height:1150px;overflow:hidden}
body{position:relative;background:var(--top-band);font-family:"Arimo",Arial,sans-serif}
.city-backdrop{position:absolute;left:0;top:55px;width:1200px;height:1012px;
  background:
    radial-gradient(ellipse 260px 520px at 600px 560px,rgba(230,220,200,.55),transparent 70%),
    linear-gradient(180deg,#9a9a98 0%,#6b6a68 18%,#4a4844 45%,#3c3a36 70%,#5a554e 100%);}
.header-panel{position:absolute;left:120px;top:55px;width:960px;height:61px;background:var(--white)}
.brand{position:absolute;left:130px;top:12px;display:flex;flex-direction:column;align-items:flex-start}
.brand-mark{width:40px;height:40px;border-radius:50%;background:var(--teal);margin-left:80px;margin-bottom:22px}
.brand-name{font-family:"Questrial",sans-serif;font-size:22px;letter-spacing:4px;color:#333;line-height:1;white-space:nowrap}
.brand-tag{font-family:"Questrial",sans-serif;font-size:9px;letter-spacing:2px;color:#333;margin-left:48px;margin-top:3px;white-space:nowrap}
.social{position:absolute;left:891px;top:18px;display:flex;gap:5px}
.social span{width:26px;height:26px;border-radius:4px;display:block}
.search{position:absolute;left:802px;top:62px;width:268px;height:36px;border:1px solid #ddd;background:var(--white);box-shadow:inset 0 1px 3px rgba(0,0,0,.12)}
.search .btn{position:absolute;right:0;top:0;width:35px;height:34px;border-left:1px solid #ddd}
.search svg{position:absolute;left:10px;top:9px}
.main-nav{position:absolute;left:120px;top:116px;width:960px;height:47px;background:var(--magenta)}
.main-nav a{position:absolute;top:0;font-family:"Questrial",sans-serif;color:var(--white);text-decoration:none;font-size:15px;height:47px;line-height:47px;white-space:nowrap}
.main-nav a.active{left:0;width:79px;background:var(--teal);text-align:center}
.hero-title{position:absolute;left:120px;top:317px;height:41px;padding:0 8px 0 7px;background:var(--teal);color:var(--white);font-family:"Questrial",sans-serif;font-size:24.5px;line-height:41px;white-space:nowrap}
.hero-line{position:absolute;left:120px;height:24px;padding:0 6px;background:var(--magenta);color:var(--white);font-family:"Questrial",sans-serif;font-size:13.6px;line-height:24px;white-space:nowrap}
.slider-dots{position:absolute;left:122px;top:563px;display:flex;gap:5px}
.slider-dots span{width:16px;height:16px;border-radius:50%;border:2px solid #bbb;background:rgba(255,255,255,.15)}
.slider-dots span.current{border-color:var(--teal);background:var(--teal-dark)}
.feature{position:absolute;top:600px;width:220px}
.feature h2{height:50px;background:var(--charcoal);color:var(--panel-title);font-family:"Questrial",sans-serif;font-weight:400;font-size:20px;line-height:56px;padding-left:11px;white-space:nowrap}
.feature .photo{height:118px}
.feature p{height:132px;background:var(--white);padding:6px 6px 0 6px;font-size:11.8px;line-height:16px;letter-spacing:-.1px;color:var(--body-text);text-align:justify}
.feature .base{height:8px;background:linear-gradient(90deg,var(--teal-dark),var(--teal))}
.partners{position:absolute;left:120px;top:936px;width:960px;height:109px;background:var(--white);display:flex;align-items:center}
.partners h3{width:138px;border-right:1px solid #ddd;height:80px;font-family:"Questrial",sans-serif;font-weight:400;color:#555;text-align:center;line-height:1}
.partners h3 .big{display:block;font-size:35px;margin-top:8px}
.partners h3 .small{display:block;font-size:22px;margin-top:2px}
.partner-list{display:flex;flex:1;justify-content:space-around;align-items:center;padding:0 10px}
.partner{display:flex;align-items:center;gap:7px;font-family:"Questrial",sans-serif;font-size:19px;color:#555;white-space:nowrap}
.partner i{display:block;width:14px;height:14px;background:#888}
.site-footer{position:absolute;left:0;top:1067px;width:1200px;height:83px;background:var(--footer-bg);text-align:center;font-size:12px;color:var(--footer-text)}
.footer-links{margin-top:23px;white-space:nowrap}
.footer-links a{color:var(--footer-text);text-decoration:none}
.footer-links .sep{margin:0 5px}
.copyright{margin-top:11px}
</style>
</head>
<body>
<div class="city-backdrop" role="img" aria-label="Night skyline of high-rise city towers"></div>

<header>
  <div class="header-panel"></div>
  <div class="brand">
    <span class="brand-mark"></span>
    <span class="brand-name">BRIGHTKEEL</span>
    <span class="brand-tag">BUSINESS CONSULTING</span>
  </div>
  <div class="social" aria-label="Social links">
    <span style="background:#3b5998"></span>
    <span style="background:#2aa3e0"></span>
    <span style="background:#c4302b"></span>
    <span style="background:#0e76a8"></span>
    <span style="background:#cb2027"></span>
    <span style="background:#dd4b39"></span>
  </div>
  <div class="search">
    <div class="btn">
      <svg width="14" height="14" viewBox="0 0 14 14"><circle cx="5.5" cy="5.5" r="4" fill="none" stroke="#aaa" stroke-width="1.5"/><line x1="8.5" y1="8.5" x2="13" y2="13" stroke="#aaa" stroke-width="2"/></svg>
    </div>
  </div>
  <nav class="main-nav">
    <a class="active" href="#">HOME</a>
    <a href="#" style="left:104px">ABOUT US</a>
    <a href="#" style="left:224px">ABOUT QIANHAI</a>
    <a href="#" style="left:386px">SERVICES</a>
    <a href="#" style="left:497px">PORTFOLIO</a>
    <a href="#" style="left:621px">PARTNERS</a>
    <a href="#" style="left:733px">OUR TEAM</a>
    <a href="#" style="left:849px">CONTACT US</a>
  </nav>
</header>

<section class="hero">
  <h1 class="hero-title">QUASI ARCHITECTO BEATAE VITAE DICTA</h1>
  <p class="hero-line" style="top:368px">SUNT EXPLICABO. NEMO ENIM IPSAM VOLUPTATEM QUIA VOLUPTAS SIT ASPER-</p>
  <p class="hero-line" style="top:404px">NATUR AUT ODIT AUT FUGIT, SED QUIA CONSEQUUNTUR MAGNI DOLORES</p>
  <p class="hero-line" style="top:440px">EOS QUI RATIONE VOLUPTATEM SEQUI NESCIUNT. NEQUE PORRO QUISQUAM</p>
  <div class="slider-dots"><span></span><span></span><span></span><span class="current"></span></div>
</section>

<section class="features">
  <article class="feature" style="left:120px">
    <h2>WELCOME!</h2>
    <div class="photo" role="img" aria-label="Business people meeting at a desk" style="background:linear-gradient(135deg,#d8d4cc,#8d9a7a 55%,#4b4a48)"></div>
    <p>consectetur adipisicing elit, sed do eiusmod tempor incididunt ut labore et dolore magna aliqua.Ut enim ad minim veniam, quis nostrud exercitation ullamco laboris nisi ut aliquip ex ea commodo consequat. Duis aute irure dolor</p>
    <div class="base"></div>
  </article>
  <article class="feature" style="left:366px">
    <h2>ABOUT QIANHAI</h2>
    <div class="photo" role="img" aria-label="Overhead view of a team around a glowing table" style="background:radial-gradient(circle at 50% 55%,#d8f4f2,#6fb4bb 35%,#2e4a55 80%)"></div>
    <p>consectetur adipisicing elit, sed do eiusmod tempor incididunt ut labore et dolore magna aliqua.Ut enim ad minim veniam, quis nostrud exercitation ullamco laboris nisi ut aliquip ex ea commodo consequat. Duis aute irure dolor</p>
    <div class="base"></div>
  </article>
  <article class="feature" style="left:612px">
    <h2>SERVICES</h2>
    <div class="photo" role="img" aria-label="Business figures assembling large puzzle pieces" style="background:linear-gradient(180deg,#f6f6f6,#dcdcdc)"></div>
    <p>consectetur adipisicing elit, sed do eiusmod tempor incididunt ut labore et dolore magna aliqua.Ut enim ad minim veniam, quis nostrud exercitation ullamco laboris nisi ut aliquip ex ea commodo consequat. Duis aute irure dolor</p>
    <div class="base"></div>
  </article>
  <article class="feature" style="left:858px">
    <h2>OUR TEAM</h2>
    <div class="photo" role="img" aria-label="Team working together at a bright office table" style="background:linear-gradient(135deg,#eef1f4,#b9c0c8 55%,#3c3f45)"></div>
    <p>consectetur adipisicing elit, sed do eiusmod tempor incididunt ut labore et dolore magna aliqua.Ut enim ad minim veniam, quis nostrud exercitation ullamco laboris nisi ut aliquip ex ea commodo consequat. Duis aute irure dolor</p>
    <div class="base"></div>
  </article>
</section>

<section class="partners">
  <h3><span class="big">OUR</span><span class="small">PARTNERS</span></h3>
  <div class="partner-list">
    <span class="partner"><i></i>Harrowgate</span>
    <span class="partner">KM Partners</span>
    <span class="partner">Vellora</span>
    <span class="partner">OSTRELL</span>
    <span class="partner"><i></i>LINKWAVE</span>
  </div>
</section>

<footer class="site-footer">
  <div class="footer-links">
    <a href="#">Home</a><span class="sep">|</span><a href="#">About Us</a><span class="sep">|</span><a href="#">About Qianhai</a><span class="sep">|</span><a href="#">Services</a><span class="sep">|</span><a href="#">Portfolio</a><span class="sep">|</span><a href="#">Partners</a><span class="sep">|</span><a href="#">Our Team</a><span class="sep">|</span><a href="#">Contact Us</a>
  </div>
  <div class="copyright">© 2013 Brightkeel &nbsp;-&nbsp; All Rights Reserved.</div>
</footer>
</body>
</html>
```